New Generation Winery needs inspiring label for special bottling

We are a family owned winery in the Rhine Valley in Germany. Check www.brandl-kohlmann.de . We have a very exciting project going: In 2014 we harvested our best vinyard and split the grapes in half. First half I have treated the way I have done it over the past 40 years. Second half I gave to my daughter who is just entering the winemaking business. She has treated it in a completely different way - her way - the way of the new generation. One of the differentiators; she has squeezed the juices with her bare feet which reduces acidity and bitterness in the wine (less tannins). This is why we want to call the wine "Kieselwind" (meaning "Pebblewind"). Please be careful when writing the "ß" . It is a German letter which replaces the "double s". It is NOT a capital B!! I Have attached a file which gives you the size of the label and another file which shows the current design of the winery labels. If possible it should pick up some elements from the current design (maybe just the colours?) but otherwise you are free. It will go on a dark green bottle, almost black. Apart from the word "Kieselwind" you need to place the grape "Riesling", the word "trocken" (means dry) and the year of the harvest "2014".

Industry/Entity Type

Brandl

Requirements
Nice to have
• Update 25.3.2015: Have a look at the attached image "Inspiration". Maybe that is a good thought starter, too. Have fun..

```html
<!DOCTYPE html>
<html lang="de">
<head>
<meta charset="utf-8">
<title>Kieselwind Riesling – Etikett</title>
<link rel="stylesheet" href="https://fonts.googleapis.com/css2?family=Cinzel:wght@500;600&family=Pinyon+Script&family=EB+Garamond:wght@400&display=swap">
<style>
  :root {
    --page: #ffffff;
    --label-cream: #f2f0dc;
    --label-line: rgba(214, 208, 170, 0.35);
    --gold: #a59b70;
    --gold-dark: #958b60;
    --footprint-red: #a8333a;
    --ink: #1b1a17;
  }
  html, body {
    margin: 0;
    padding: 0;
    width: 1200px;
    height: 848px;
    overflow: hidden;
    background: var(--page);
  }
  .canvas {
    position: relative;
    width: 1200px;
    height: 848px;
  }
  .label {
    position: absolute;
    left: 250px;
    top: 74px;
    width: 700px;
    height: 700px;
    overflow: hidden;
    background-color: var(--label-cream);
    background-image: repeating-linear-gradient(
      to bottom,
      transparent 0,
      transparent 6px,
      var(--label-line) 6px,
      var(--label-line) 8px
    );
    text-align: center;
  }
  .label > * {
    position: absolute;
    left: 0;
    right: 0;
    margin: 0;
    transform: translateY(-50%);
  }
  .winery {
    top: 106px;
    display: flex;
    justify-content: center;
    align-items: center;
    gap: 18px;
    font-family: "Cinzel", serif;
    font-weight: 500;
    font-size: 28px;
    line-height: 1;
    letter-spacing: 1px;
    color: var(--ink);
  }
  .winery-dot {
    width: 44px;
    height: 44px;
    border-radius: 50%;
    background: var(--gold);
  }
  .wine-name {
    top: 326px;
    display: flex;
    justify-content: center;
    align-items: center;
    font-family: "Cinzel", serif;
    font-weight: 600;
    font-size: 64px;
    letter-spacing: 3px;
    color: var(--gold-dark);
    line-height: 1;
  }
  .wine-name .initial {
    font-size: 80px;
  }
  .footprints {
    display: inline-block;
    width: 44px;
    height: 84px;
    margin: 0 4px;
  }
  .grape {
    top: 520px;
    font-family: "Pinyon Script", cursive;
    font-size: 108px;
    line-height: 1.1;
    color: var(--ink);
  }
  .style {
    top: 606px;
    font-family: "EB Garamond", serif;
    font-size: 21px;
    line-height: 1;
    letter-spacing: 2px;
    color: var(--ink);
  }
  .vintage {
    top: 650px;
    font-family: "EB Garamond", serif;
    font-size: 29px;
    line-height: 1;
    letter-spacing: 1px;
    color: var(--ink);
  }
</style>
</head>
<body>
  <main class="canvas">
    <section class="label">
      <div class="winery">
        <span class="winery-name">BRANDL</span>
        <span class="winery-dot" aria-hidden="true"></span>
        <span class="winery-name">KOHLMANN</span>
      </div>
      <h1 class="wine-name">
        <span class="initial">K</span>IESEL<svg class="footprints" viewBox="0 0 44 84" role="img" aria-label="Two red bare footprints"><rect x="4" y="2" width="36" height="80" rx="16" fill="var(--footprint-red)"/></svg>WIND
      </h1>
      <p class="grape">Riesling</p>
      <p class="style">TROCKEN</p>
      <p class="vintage">2014</p>
    </section>
  </main>
</body>
</html>
```